design a construction company business card

Design business card around our logo. Card must have all the typical info: name, title, address, phone, email, business name, etc. Somewhere on the card I would like to see our motto "Built on integrity... Inspired by commitment." Consider adding a splash of bright orange to the card to complement the blues and silvers/grays in the logo. We are open to metallic inks, textures, etc. We would like to see options on both light and dark backgrounds. The font in the logo is Euro Technic Extended Regular.

```html
<!DOCTYPE html>
<html lang="en">
<head>
<meta charset="UTF-8">
<title>Halden Contracting – Business Card</title>
<link href="https://fonts.googleapis.com/css2?family=Michroma&display=swap" rel="stylesheet">
<style>
  :root {
    --page-bg: #f3f3f3;
    --card-white: #f7f7f6;
    --brand-blue: #2a52b8;
    --frame-blue: #2f7fd0;
    --ink-gray: #4a4a4a;
    --band-black: #0c0c0c;
    --logo-gray: #5a5a5a;
    --text-white: #ffffff;
    --text-soft: #e6e6e6;
  }
  * { margin: 0; padding: 0; box-sizing: border-box; }
  html, body {
    width: 1200px; height: 1200px; overflow: hidden;
    background: var(--page-bg);
    font-family: "Michroma", sans-serif;
  }
  .canvas { position: relative; width: 1200px; height: 1200px; }

  .card {
    position: absolute; left: 222px; width: 756px; height: 424px;
    background: var(--card-white); border-radius: 22px; overflow: hidden;
  }
  .card--front { top: 130px; }
  .card--back { top: 608px; }

  .front-frame {
    position: absolute; inset: 16px;
    border: 1.5px solid var(--frame-blue); border-radius: 18px;
  }
  .wordmark {
    position: absolute; left: 0; right: 0;
    display: flex; align-items: center; justify-content: center; gap: 12px;
    text-transform: uppercase; letter-spacing: 1px; white-space: nowrap;
  }
  .wordmark__square { width: 16px; height: 16px; }
  .card--front .wordmark { top: 176px; font-size: 24px; color: var(--brand-blue); }
  .card--front .wordmark__square { background: var(--brand-blue); }

  .motto {
    position: absolute; left: 0; right: 0; top: 360px;
    text-align: center; font-size: 17px; color: var(--ink-gray);
    letter-spacing: 0.2px;
  }

  .back-band {
    position: absolute; left: 0; right: 0; top: 48px; height: 328px;
    background: var(--band-black);
  }
  .person-name {
    position: absolute; left: 0; right: 0; top: 30px;
    text-align: center; font-size: 20px; color: var(--text-white);
    letter-spacing: 0.5px; -webkit-text-stroke: 0.6px var(--text-white);
  }
  .person-title {
    position: absolute; left: 0; right: 0; top: 60px;
    text-align: center; font-size: 11px; color: var(--text-soft);
  }
  .card--back .wordmark { top: 168px; font-size: 24px; color: var(--logo-gray); }
  .card--back .wordmark__square { background: var(--logo-gray); }

  .contact-list {
    position: absolute; left: 0; right: 0; top: 242px;
    list-style: none; text-align: center;
    font-size: 11px; line-height: 19px; color: var(--text-white);
  }
</style>
</head>
<body>
  <main class="canvas">
    <section class="card card--front">
      <div class="front-frame"></div>
      <div class="wordmark">
        <span class="wordmark__square"></span>
        <span class="wordmark__name">Halden Contracting, Inc.</span>
      </div>
      <p class="motto">Built on integrity... Inspired by commitment</p>
    </section>

    <section class="card card--back">
      <div class="back-band">
        <h1 class="person-name">MARA VELLAND</h1>
        <p class="person-title">PROJECT ENGINEER</p>
        <div class="wordmark">
          <span class="wordmark__square"></span>
          <span class="wordmark__name">Halden Contracting, Inc.</span>
        </div>
        <ul class="contact-list">
          <li>14 Granite Row, Suite 210</li>
          <li>+1 555 014 2290</li>
          <li>info@haldencontracting.com</li>
          <li>www.haldencontracting.com</li>
        </ul>
      </div>
    </section>
  </main>
</body>
</html>
```